General Power Point Presentation Pack

Hello Designers,

I am after a professional looking Microsoft PowerPoint deck that can be used for our corporate presentations. The pack should include a:

Title Page
Tittle and Content Page
Section Header Sheet
Two Content Page
Title Only Page
Blank Page
Content with Caption Page
Picture with Caption Page

I have included my brand guidelines and colours. I have also included some photos you may be able to use. Can you please ensure the pack has page numbering and that when you print it that it can be printed to full A4 Page.

Industry/Entity Type

Property Development & Construction

Requirements
Must have
• Prefer a white or very light coloured background

```html
<!DOCTYPE html>
<html lang="en">
<head>
<meta charset="utf-8">
<title>Keystone Presentation Template</title>
<link href="https://fonts.googleapis.com/css2?family=Montserrat:wght@300;700&family=Roboto:wght@300;400;500;700;900&display=swap" rel="stylesheet">
<style>
  :root {
    --gold: #D9A861;
    --cream: #EFE9D8;
    --rust: #CF602F;
    --blush: #F6E2DC;
    --peach: #EEC4B2;
    --white: #FFFFFF;
    --ink: #111111;
    --heading: #3A3A3A;
    --muted: #A7A7A7;
    --body-gray: #8C8C8C;
  }
  * { box-sizing: border-box; margin: 0; padding: 0; }
  html, body { width: 800px; height: 1200px; overflow: hidden; background: var(--white); }
  body { position: relative; font-family: "Roboto", Arial, sans-serif; color: var(--ink); }

  .brand-title { position: absolute; left: 412px; top: 40px; font-family: "Montserrat", Arial, sans-serif; font-weight: 700; font-size: 50px; letter-spacing: 3px; color: var(--heading); line-height: 1; }
  .brand-sub { position: absolute; left: 418px; top: 106px; font-family: "Montserrat", Arial, sans-serif; font-weight: 300; font-size: 21px; letter-spacing: 9px; color: var(--heading); }
  .palette { position: absolute; left: 594px; top: 103px; display: flex; }
  .swatch { width: 31px; height: 31px; border-radius: 50%; margin-right: -3px; box-shadow: 0 2px 5px rgba(0,0,0,.18); }

  .slide { position: absolute; width: 360px; height: 203px; overflow: hidden; background: var(--white); box-shadow: 0 10px 22px rgba(0,0,0,.16); }
  .photo { position: absolute; }
  .rule { position: absolute; left: 20px; right: 18px; top: 15px; height: 1px; background: var(--cream); }
  .mark { position: absolute; left: 20px; top: 5px; font-size: 5px; font-weight: 700; color: var(--gold); letter-spacing: .3px; }
  .page-label { position: absolute; right: 18px; top: 10px; font-size: 3.6px; color: #333; letter-spacing: .1px; }
  .footer-url { position: absolute; bottom: 7px; font-size: 3.6px; color: var(--muted); }
  .h-big { font-weight: 900; font-size: 15px; line-height: 1.05; letter-spacing: .8px; color: var(--ink); }
  .h-soft { font-weight: 700; font-size: 15px; line-height: 1.05; color: #222; }
  .copy { font-size: 4.6px; line-height: 1.55; color: var(--muted); font-weight: 300; }
  .copy-dark { font-size: 3.8px; line-height: 1.9; color: #3b3b3b; }
  .kicker { font-size: 3.8px; letter-spacing: .4px; color: #555; }

  /* title slide */
  .cover { left: 20px; top: 108px; background: var(--rust); }
  .cover .photo { inset: 0; background: linear-gradient(100deg, rgba(255,255,255,.06), rgba(0,0,0,.03) 40%, rgba(255,255,255,.05)); }
  .cover-lockup { position: absolute; left: 100px; top: 78px; display: flex; align-items: center; }
  .cover-square { width: 22px; height: 22px; background: var(--gold); margin-right: 8px; }
  .cover-divider { width: 1px; height: 38px; background: var(--gold); margin-right: 10px; }
  .cover-name { font-size: 22px; font-weight: 700; color: var(--gold); line-height: 1; }
  .cover-tag { font-size: 6.6px; letter-spacing: 2.6px; color: var(--gold); margin-top: 5px; }

  .s2 { left: 419px; top: 194px; }
  .s3 { left: 20px; top: 367px; }
  .s4 { left: 421px; top: 452px; }
  .s5 { left: 20px; top: 626px; }
  .s6 { left: 420px; top: 712px; }
  .s7 { left: 20px; top: 885px; }
  .s8 { left: 420px; top: 971px; }

  .service-card { position: absolute; left: 138px; top: 45px; width: 202px; height: 113px; background: var(--white); box-shadow: 0 2px 8px rgba(0,0,0,.1); }
  .service-card .item { position: absolute; left: 19px; }
  .item-title { font-size: 4.4px; color: #222; }
  .item-text { font-size: 3.6px; color: var(--muted); margin-top: 3px; }
  .right-item { position: absolute; left: 216px; width: 120px; }
  .right-item .t { font-size: 5px; font-weight: 500; color: #333; margin-bottom: 3px; }
  .right-item .d { font-size: 3.7px; color: #444; line-height: 1.9; }
  .para { font-size: 4.4px; line-height: 1.6; color: var(--muted); font-weight: 300; width: 312px; }
</style>
</head>
<body>
  <h1 class="brand-title">KEYSTONE</h1>
  <div class="brand-sub">TEMPLATE</div>
  <div class="palette">
    <span class="swatch" style="background:var(--gold)"></span>
    <span class="swatch" style="background:var(--cream)"></span>
    <span class="swatch" style="background:var(--rust)"></span>
    <span class="swatch" style="background:var(--blush)"></span>
    <span class="swatch" style="background:var(--white)"></span>
  </div>

  <!-- Title page -->
  <section class="slide cover">
    <div class="photo" role="img" aria-label="Faint apartment building facade behind an orange overlay"></div>
    <div class="cover-lockup">
      <span class="cover-square"></span>
      <span class="cover-divider"></span>
      <div>
        <div class="cover-name">Keystone</div>
        <div class="cover-tag">PRESENTATION TEMPLATE</div>
      </div>
    </div>
  </section>

  <!-- Page 2 -->
  <section class="slide s2">
    <div class="photo" role="img" aria-label="Bright apartment dining area with a warm peach tint" style="left:0;top:0;width:162px;height:203px;background:linear-gradient(160deg,#C9785A,#D99C83 55%,#E0AE96);"></div>
    <div class="rule"></div>
    <div class="mark">Keystone</div>
    <div class="page-label">COMPANY PRESENTATION &nbsp;| &nbsp;2</div>
    <div class="h-soft" style="position:absolute;left:21px;top:60px;color:var(--white);">Exclusive<br>service</div>
    <p class="copy" style="position:absolute;left:21px;top:104px;width:102px;color:rgba(255,255,255,.85);font-size:3.8px;line-height:1.95;">Etiam vitae dui congue, semper quam vitae, luctus ligula. Sed posuere nunc in leo commod else cuprum less. Etiam vitae dui congue, semper quam vitae, luctus. Integer a turpis quam. Donec convallis orci eu orci rutrum, ac venenatis diam mollis.</p>
    <div class="service-card">
      <div class="item" style="top:29px"><div class="item-title">SERVICE</div><div class="item-text">Etiam vitae dui congue, semper quam vitae, luctus ligula. Sed posuere nunc.</div></div>
      <div class="item" style="top:79px"><div class="item-title">SERVICE</div><div class="item-text">Etiam vitae dui congue, semper quam vitae, luctus ligula. Sed posuere nunc.</div></div>
    </div>
    <div class="footer-url" style="left:162px">www.yourdomain.com</div>
  </section>

  <!-- Page 3 -->
  <section class="slide s3">
    <svg class="photo" width="360" height="203" style="left:0;top:0" role="img" aria-label="Modern brick and glass apartment buildings along a street at dusk">
      <defs><linearGradient id="bldgA" x1="0" y1="0" x2="0" y2="1"><stop offset="0" stop-color="#B9B3C0"/><stop offset=".55" stop-color="#9C8C86"/><stop offset="1" stop-color="#7E8A6E"/></linearGradient></defs>
      <polygon points="0,0 143,0 173,203 0,203" fill="url(#bldgA)"/>
      <polygon points="143,0 150,0 180,203 173,203" fill="var(--blush)"/>
    </svg>
    <div class="rule"></div>
    <div class="mark">Keystone</div>
    <div class="page-label">COMPANY PRESENTATION &nbsp;| &nbsp;3</div>
    <h2 class="h-big" style="position:absolute;left:187px;top:43px;">BUSINESS<br>INTRODUCTION</h2>
    <p class="copy" style="position:absolute;left:187px;top:90px;width:115px;">Ut wisi enim ad minim veniam, quis nostrud exerci tation ullamcorper nibh euismod tincidunt ut laoreet dolore magna aliquam erat volutpat. Ut wisi enim ad minim veniam, quis nostrud exerci. exerci tation ullamcorper nibh euismod tincidunt ut .</p>
    <div class="footer-url" style="left:161px">www.yourdomain.com</div>
  </section>

  <!-- Page 4 -->
  <section class="slide s4">
    <svg class="photo" width="360" height="203" style="left:0;top:0" role="img" aria-label="Modern brick and glass apartment buildings along a street at dusk">
      <defs><linearGradient id="bldgB" x1="0" y1="0" x2="0" y2="1"><stop offset="0" stop-color="#BBB6C4"/><stop offset=".55" stop-color="#9E8D86"/><stop offset="1" stop-color="#7F8B70"/></linearGradient></defs>
      <polygon points="207,0 214,0 183,203 176,203" fill="var(--blush)"/>
      <polygon points="214,0 360,0 360,203 183,203" fill="url(#bldgB)"/>
    </svg>
    <div class="rule" style="right:20px"></div>
    <div class="mark" style="left:18px">Keystone</div>
    <div class="page-label">COMPANY PRESENTATION &nbsp;| &nbsp;4</div>
    <h2 class="h-big" style="position:absolute;left:18px;top:27px;">BUSINESS<br>INTRODUCTION</h2>
    <p class="copy" style="position:absolute;left:18px;top:75px;width:115px;">Ut wisi enim ad minim veniam, quis nostrud exerci tation ullamcorper nibh euismod tincidunt ut laoreet dolore magna aliquam erat volutpat. Ut wisi enim ad minim veniam, quis nostrud exerci. exerci tation ullamcorper nibh euismod tincidunt ut .</p>
    <div class="footer-url" style="left:160px">www.yourdomain.com</div>
  </section>

  <!-- Page 5 -->
  <section class="slide s5">
    <div class="photo" role="img" aria-label="Apartment complex with palm trees and landscaped entry path at dusk" style="left:0;top:0;width:173px;height:109px;background:linear-gradient(180deg,#8DA2BC,#A58E84 50%,#5E6B4E);"></div>
    <div class="photo" style="left:0;top:109px;width:173px;height:94px;background:var(--peach);"></div>
    <div class="rule" style="left:173px"></div>
    <div class="mark">Keystone</div>
    <div class="page-label">COMPANY PRESENTATION &nbsp;| &nbsp;5</div>
    <h2 class="h-soft" style="position:absolute;left:22px;top:126px;">Our Service</h2>
    <div class="kicker" style="position:absolute;left:22px;top:146px;">WORDS ABOUT SERVICE'S</div>
    <p class="copy-dark" style="position:absolute;left:22px;top:156px;width:135px;">Etiam vitae dui congue, semper quam vitae, luctus ligula. Sed posuere nunc in leo commod else cuprum less. Etiam vitae dui congue, semper quam vitae, luctus. Integer a turpis quam. Donec</p>
    <div class="right-item" style="top:35px"><div class="t">Put Title Hoes Here</div><div class="d">Etiam vitae dui congue, semper quam vitae, luctus ligula. Sed posuere nunc in leo commod else cuprum less..</div></div>
    <div class="right-item" style="top:92px"><div class="t">Put Title Hoes Here</div><div class="d">Etiam vitae dui congue, semper quam vitae, luctus ligula. Sed posuere nunc in leo commod else cuprum less.</div></div>
    <div class="right-item" style="top:152px"><div class="t">Put Title Hoes Here</div><div class="d">Etiam vitae dui congue, semper quam vitae, luctus ligula. Sed posuere nunc in leo commod else cuprum.</div></div>
    <div class="footer-url" style="left:161px">www.yourdomain.com</div>
  </section>

  <!-- Page 6 -->
  <section class="slide s6">
    <div class="photo" role="img" aria-label="Light open-plan living and dining room with large windows onto trees" style="inset:0;background:linear-gradient(100deg,#E4DED6,#CFC7BC 45%,#B9B7A6 70%,#C8BFB2);"></div>
    <div class="photo" style="left:0;top:0;width:72px;height:15px;background:rgba(120,105,95,.45);"></div>
    <div class="rule"></div>
    <div class="mark">Keystone</div>
    <div class="page-label">COMPANY PRESENTATION &nbsp;| &nbsp;6</div>
    <div style="position:absolute;left:22px;top:78px;width:91px;height:101px;background:rgba(238,184,160,.88);"></div>
    <h2 class="h-soft" style="position:absolute;left:30px;top:95px;color:#333;">Exclusive</h2>
    <p class="copy-dark" style="position:absolute;left:27px;top:114px;width:82px;">Etiam vitae dui congue, semper quam vitae, luctus ligula. Sed posuere nunc in leo commod else cuprum less. Etiam vitae dui congue, semper quam vitae, luctus. Integer a turpis quam. Donec convallis orci eu orci rutrum, ac venenatis diam mollis.</p>
  </section>

  <!-- Page 7 -->
  <section class="slide s7">
    <div class="photo" role="img" aria-label="Light open-plan living and dining room with large windows onto trees" style="inset:0;background:linear-gradient(100deg,#E4DED6,#CFC7BC 45%,#B9B7A6 70%,#C8BFB2);"></div>
    <div class="photo" style="left:0;top:0;width:72px;height:15px;background:rgba(120,105,95,.45);"></div>
    <svg class="photo" width="360" height="203" style="left:0;top:0" aria-hidden="true">
      <polygon points="322,0 360,0 360,30 180,203 140,203" fill="var(--cream)"/>
    </svg>
    <div class="rule"></div>
    <div class="mark">Keystone</div>
    <div class="page-label">COMPANY PRESENTATION &nbsp;| &nbsp;7</div>
    <div style="position:absolute;left:15px;top:111px;width:133px;height:92px;background:var(--white);"></div>
    <h2 class="h-soft" style="position:absolute;left:31px;top:128px;color:#333;">WELCOME</h2>
    <p class="copy-dark" style="position:absolute;left:31px;top:147px;width:105px;">commun vocabules. Omnicos directe al desirabilite de un nov lingua franca: On refusa continuar payar custosi traductores.</p>
    <div class="footer-url" style="left:161px">www.yourdomain.com</div>
  </section>

  <!-- Page 8 -->
  <section class="slide s8">
    <div class="rule"></div>
    <div class="mark">Keystone</div>
    <div class="page-label">COMPANY PRESENTATION &nbsp;| &nbsp;8</div>
    <h2 class="h-soft" style="position:absolute;left:22px;top:23px;">Our Service</h2>
    <div class="kicker" style="position:absolute;left:22px;top:42px;">WORDS ABOUT SERVICE'S</div>
    <p class="para" style="position:absolute;left:22px;top:64px;">Ut wisi enim ad minim veniam, quis nostrud exerci tation ullamcorper nibh euismod tincidunt ut laoreet dolore magna aliquam erat volutpat. Ut wisi enim ad minim veniam, quis nostrud exerci. exerci tation ullamcorper nibh euismod tincidunt ut .</p>
    <p class="para" style="position:absolute;left:22px;top:88px;">Ut wisi enim ad minim veniam, quis nostrud exerci tation ullamcorper nibh euismod tincidunt ut laoreet dolore magna aliquam erat volutpat. Ut wisi enim ad minim veniam, quis nostrud exerci. exerci tation ullamcorper nibh euismod tincidunt ut .</p>
    <p class="para" style="position:absolute;left:22px;top:112px;">Ut wisi enim ad minim veniam, quis nostrud exerci tation ullamcorper nibh euismod tincidunt ut laoreet dolore magna aliquam erat volutpat. Ut wisi enim ad minim veniam, quis nostrud exerci. exerci tation ullamcorper nibh euismod tincidunt ut .</p>
    <p class="para" style="position:absolute;left:22px;top:139px;">Ut wisi enim ad minim veniam, quis nostrud exerci tation ullamcorper nibh euismod tincidunt ut laoreet dolore magna aliquam erat volutpat. Ut wisi enim ad minim veniam, quis nostrud exerci. exerci tation ullamcorper nibh euismod tincidunt ut .</p>
    <div class="footer-url" style="left:161px">www.yourdomain.com</div>
  </section>
</body>
</html>
```